Tallow Inks needs a new Webpage for their collection of ballpens

We at Tallow inks need a brand new webpage to represent our company and range of products. We need a product based website to focus purely on our collection. The web design must bring about a perception of high quality International brand but still affordable in price. Since there are only 5 products, they must all feature on the cover page itself.

Target Market(s)

Stationary Wholesale and retail

Industry/Entity Type

It Company

Number of Pages Required

1 page

Requirements
Must have
• pls see www.quambrite.example to derive inspiration
Should not have
• stock images
• abstract images
• random pen images

```html
<!DOCTYPE html>
<html lang="en">
<head>
<meta charset="utf-8">
<title>Tallow Inks</title>
<link rel="stylesheet" href="https://fonts.googleapis.com/css2?family=Roboto+Condensed:wght@700&family=Arimo:wght@400&display=swap">
<style>
  :root {
    --brand-blue: #1b609f;
    --brand-blue-dark: #104a80;
    --header-bg: #ebebeb;
    --hero-top: #e6e7e9;
    --hero-bottom: #f4f4f4;
    --divider: #cccccc;
    --rule: #dcdcdc;
    --footer-bg: #f5f5f5;
  }
  * { margin: 0; padding: 0; box-sizing: border-box; }
  html, body { width: 1200px; height: 708px; overflow: hidden; }
  body {
    position: relative;
    font-family: "Arimo", Arial, sans-serif;
    color: var(--brand-blue);
    background: var(--footer-bg);
  }
  .site-header {
    position: absolute; left: 0; top: 0; width: 1200px; height: 56px;
    background: var(--header-bg);
    border-bottom: 3px solid var(--brand-blue);
  }
  .brand {
    position: absolute; left: 159px; top: 9px;
    font-family: "Arimo", Arial, sans-serif;
    font-size: 34px; letter-spacing: 7px; line-height: 34px;
    color: var(--brand-blue);
  }
  .main-nav { position: absolute; top: 20px; left: 806px; display: flex; gap: 30px; }
  .main-nav a { color: var(--brand-blue); text-decoration: none; font-size: 14px; }
  .hero {
    position: absolute; left: 0; top: 56px; width: 1200px; height: 515px;
    background: linear-gradient(var(--hero-top), var(--hero-bottom));
  }
  .product-title {
    position: absolute; left: 157px; top: 146px;
    font-family: "Roboto Condensed", "Arial Narrow", sans-serif;
    font-weight: 700; font-size: 45px; line-height: 50px;
  }
  .product-specs { position: absolute; left: 190px; top: 219px; list-style: none; }
  .product-specs li { font-size: 22px; line-height: 36px; }
  .cta {
    position: absolute; left: 418px; top: 352px; width: 110px; height: 24px;
    border: 1.5px solid var(--brand-blue); color: var(--brand-blue);
    font-size: 14px; line-height: 21px; text-align: center; text-decoration: none;
  }
  .product-lineup {
    position: absolute; left: 746px; top: 44px; width: 318px; height: 396px;
    background: linear-gradient(90deg, #d9dadc, #e3e4e6 45%, #d9dadc);
    border-radius: 6px;
  }
  .zoom-tag {
    position: absolute; left: 915px; top: 337px; width: 19px; height: 72px;
    background: #e2e3e5;
  }
  .zoom-tag span {
    position: absolute; left: 1px; top: 26px;
    writing-mode: vertical-rl; font-size: 13px; letter-spacing: 2px;
  }
  .slider-nav { position: absolute; left: 556px; top: 455px; display: flex; gap: 9px; }
  .site-footer {
    position: absolute; left: 0; top: 571px; width: 1200px; height: 137px;
    border-top: 7px solid var(--divider);
    background: var(--footer-bg);
  }
  .footer-col { position: absolute; top: 25px; width: 238px; }
  .footer-col h2 {
    font-family: "Roboto Condensed", "Arial Narrow", sans-serif;
    font-weight: 700; font-size: 16px; line-height: 18px;
    padding-bottom: 3px; border-bottom: 3px solid var(--rule);
  }
  .footer-col p { font-size: 14px; line-height: 18px; margin-top: 12px; white-space: nowrap; }
  .col-find { left: 158px; }
  .col-contact { left: 478px; }
  .col-follow { left: 798px; }
  .social-list { display: flex; gap: 5px; margin-top: 11px; margin-left: 2px; }
  .social-list span {
    width: 24px; height: 24px; border-radius: 50%; background: var(--brand-blue);
  }
</style>
</head>
<body>
  <header class="site-header">
    <div class="brand">TALLOW</div>
    <nav class="main-nav">
      <a href="#">HOME</a>
      <a href="#">ABOUT US</a>
      <a href="#">CONTACT</a>
    </nav>
  </header>

  <section class="hero">
    <h1 class="product-title">TALLOW VELA</h1>
    <ul class="product-specs">
      <li>- TIP SIZE: 0.7MM</li>
      <li>- 5PCS POUCH</li>
      <li>- AVAILABLE IN BLUE/ BLACK INK</li>
    </ul>
    <a class="cta" href="#">TAKE IT NOW!</a>

    <div class="product-lineup" role="img" aria-label="Five Tallow ballpoint pens standing side by side, the blue Vela pen highlighted in the centre"></div>

    <div class="zoom-tag">
      <svg width="19" height="20" viewBox="0 0 19 20" aria-hidden="true">
        <circle cx="9" cy="9" r="5" fill="none" stroke="#1b609f" stroke-width="1.6"/>
        <line x1="12.5" y1="12.5" x2="16" y2="16" stroke="#1b609f" stroke-width="2"/>
        <line x1="9" y1="6.5" x2="9" y2="11.5" stroke="#1b609f" stroke-width="1.3"/>
        <line x1="6.5" y1="9" x2="11.5" y2="9" stroke="#1b609f" stroke-width="1.3"/>
      </svg>
      <span>zoom</span>
    </div>

    <div class="slider-nav">
      <svg width="39" height="39" viewBox="0 0 39 39" aria-label="Previous">
        <defs>
          <radialGradient id="btnGrad" cx="40%" cy="35%" r="70%">
            <stop offset="0" stop-color="#4a97d6"/>
            <stop offset="1" stop-color="#104a80"/>
          </radialGradient>
        </defs>
        <circle cx="19.5" cy="19.5" r="19" fill="url(#btnGrad)"/>
        <path d="M23 10 L13 19.5 L23 29" fill="none" stroke="#0c3a66" stroke-width="5"/>
      </svg>
      <svg width="39" height="39" viewBox="0 0 39 39" aria-label="Next">
        <circle cx="19.5" cy="19.5" r="19" fill="url(#btnGrad)"/>
        <path d="M16 10 L26 19.5 L16 29" fill="none" stroke="#0c3a66" stroke-width="5"/>
      </svg>
    </div>
  </section>

  <footer class="site-footer">
    <div class="footer-col col-find">
      <h2>HOW TO FIND</h2>
      <p>27-410 Fenwick Road, Brookhaven<br>USA 200-415-730</p>
    </div>
    <div class="footer-col col-contact">
      <h2>CONTACT US</h2>
      <p>Tel. : 0870041526 K.Marsh<br>Email. : contact@tallowinks.example</p>
    </div>
    <div class="footer-col col-follow">
      <h2>FOLLOW</h2>
      <div class="social-list">
        <span></span><span></span><span></span><span></span><span></span>
      </div>
    </div>
  </footer>
</body>
</html>
```